Re-branding stationary for Company

Corvane Diamonds is a diamond trading company that has been established since more then 30years.

We are currently looking to re-design our current logo design into something more modern and more appealing the the new generation. Small changes are what we are looking for that will give our company a little more modern look and a new appeal.
The design should be on similar lines to what our current logo is, but we are definitely wanting to have some modern changes to this.
Along with this, we are looking to have design for complete stationary including, business cards, envelopes, letterheads, etc..

Attached is our current logo, can use this as a base point towards creating a new design.
Updates

Project Deadline Extended Reason: Am still looking for wonderful and amazingly creative design for my company, a facelift with a little modern touchHave provided you with a current logo of the company as inspiration to make something new and unique. PLEASE DO NOT USE COPY THE LOGO FILE AS IT IS! Added Wednesday, May 6, 2015

Target Market(s)

We are a company established since over 30 years, and want to maintain our core fundamental values which is portrayed through our logo. Use this as a base into creating new modern design.

Industry/Entity Type

It Company

Font styles to use
Serif
Sans Serif
Decorative
Script

Requirements
Must have
• A modern touch
• Color combination should be similar in terms with what we currently use in attached design.
Nice to have
• Want that the design is appealing using simple but yet modern features to change and restructure the current company logo.
Should not have
• Not looking more multi colored design
• Not gotta be too overly extravagant

```html
<!DOCTYPE html>
<html lang="en">
<head>
<meta charset="utf-8">
<title>Corvane Diamonds – Stationery</title>
<link href="https://fonts.googleapis.com/css2?family=Arimo:wght@400;700&display=swap" rel="stylesheet">
<style>
  :root {
    --navy: #0b2a6b;
    --grey: #a9abb0;
    --paper: #ffffff;
    --backdrop: #eeeff0;
    --ink: #3a3a3a;
    --edge: #dcdde0;
  }
  * { margin: 0; padding: 0; box-sizing: border-box; }
  html, body { width: 1200px; height: 937px; overflow: hidden; }
  body {
    background: var(--backdrop);
    font-family: "Arimo", Arial, sans-serif;
    color: var(--ink);
    position: relative;
  }
  .sheet {
    position: absolute;
    background: var(--paper);
    border: 1px solid var(--edge);
    overflow: hidden;
  }

  /* Footer: plain straight navy band with a thin grey rule above */
  .footer-band {
    position: absolute; left: 0; bottom: 0; width: 100%;
    height: var(--band-h, 26px);
    background: var(--navy);
  }
  .footer-band::before {
    content: ""; position: absolute; left: 0; right: 0;
    top: calc(var(--rule-gap, 6px) * -1 - var(--rule-h, 4px));
    height: var(--rule-h, 4px);
    background: var(--grey);
  }

  .brand { position: absolute; display: flex; align-items: center; gap: 6px; }
  .brand-name { font-weight: 700; color: var(--navy); white-space: nowrap; }
  .brand-mark { background: var(--navy); flex: none; }

  /* Letterhead */
  .letterhead { left: 185px; top: 68px; width: 386px; height: 544px; }
  .letterhead .brand { left: 38px; top: 44px; }
  .letterhead .brand-name { font-size: 17px; }
  .letterhead .brand-mark { width: 30px; height: 30px; }
  .contact-list { position: absolute; right: 16px; top: 22px; list-style: none; text-align: right; }
  .contact-list li { font-size: 4.6px; line-height: 8px; color: var(--ink); display: flex; justify-content: flex-end; align-items: center; gap: 3px; }
  .contact-list li::after { content: ""; width: 5px; height: 5px; border-radius: 50%; background: var(--navy); }
  .letter { position: absolute; left: 38px; top: 136px; width: 300px; font-size: 5.4px; line-height: 7.6px; }
  .letter p { margin-bottom: 7px; }
  .letter .gap { margin-bottom: 20px; }
  .letter strong { font-weight: 700; }
  .signature { width: 28px; height: 16px; background: linear-gradient(90deg, #d9d9d9, #9a9a9a); border-radius: 2px; margin: 2px 0 8px; }
  .letterhead .footer-band { --band-h: 24px; --rule-h: 5px; --rule-gap: 5px; }

  /* Folder sheet */
  .cover { left: 636px; top: 40px; width: 458px; height: 576px; }
  .cover .brand { left: 90px; top: 254px; gap: 10px; }
  .cover .brand-name { font-size: 28px; }
  .cover .brand-mark { width: 52px; height: 52px; }
  .cover .footer-band { --band-h: 24px; --rule-h: 5px; --rule-gap: 5px; }

  /* Business cards */
  .card { width: 177px; height: 100px; border-radius: 8px; }
  .card-front { left: 45px; top: 659px; }
  .card-back { left: 45px; top: 785px; }
  .card-front .brand { left: 50px; top: 16px; gap: 3px; }
  .card-front .brand-name { font-size: 7.5px; }
  .card-front .brand-mark { width: 12px; height: 12px; }
  .holder { position: absolute; left: 18px; top: 46px; text-align: center; width: 80px; }
  .holder .name { font-size: 5.6px; letter-spacing: 0.5px; color: var(--navy); }
  .holder .role, .holder .addr { font-size: 3.8px; line-height: 5.4px; }
  .holder .role { margin-bottom: 4px; }
  .card-contacts { position: absolute; left: 104px; top: 44px; list-style: none; border-left: 0.6px solid var(--grey); padding-left: 4px; }
  .card-contacts li { font-size: 3.8px; line-height: 5.4px; display: flex; align-items: center; gap: 2px; }
  .card-contacts li::before { content: ""; width: 3.5px; height: 3.5px; border-radius: 50%; background: var(--navy); }
  .card-front .footer-band { --band-h: 9px; --rule-h: 2px; --rule-gap: 2px; }
  .card-back .brand { left: 28px; top: 32px; gap: 4px; }
  .card-back .brand-name { font-size: 11px; }
  .card-back .brand-mark { width: 18px; height: 18px; }

  /* Envelopes */
  .envelope-front { left: 265px; top: 671px; width: 432px; height: 209px; }
  .envelope-front .brand { left: 10px; top: 22px; gap: 5px; }
  .envelope-front .brand-name { font-size: 13px; }
  .envelope-front .brand-mark { width: 24px; height: 24px; }
  .envelope-front .footer-band { --band-h: 26px; --rule-h: 5px; --rule-gap: 5px; }
  .envelope-back { left: 736px; top: 671px; width: 432px; height: 208px; }
  .flap {
    position: absolute; left: 0; top: 0; width: 100%; height: 74px;
    background: var(--navy);
    border-radius: 0 0 36px 36px;
    display: flex; align-items: center; justify-content: center;
  }
  .flap .web { color: #ffffff; font-size: 13px; letter-spacing: 2px; }
</style>
</head>
<body>

<section class="sheet letterhead">
  <div class="brand"><span class="brand-name">Corvane Diamonds</span><span class="brand-mark"></span></div>
  <ul class="contact-list">
    <li>012 345 6789</li>
    <li>012 345 6790</li>
    <li>mail@corvanediamonds.com</li>
    <li>www.corvanediamonds.com</li>
    <li>88 Harbor Lane, Antwerp 2018</li>
  </ul>
  <div class="letter">
    <p>July 2, 2012</p>
    <p><strong>Dear Cili,</strong><br>ABC Building, def St., Country Name</p>
    <p class="gap">is simply dummy text of the printing and typesetting industry. Lorem Ipsum has been the industry's standard dummy text ever since the 1500s, when an unknown printer took a galley of type and scrambled it to make a type specimen book. It has survived not only five centuries, but also the leap into electronic typesetting, remaining essentially unchanged. It was popularised in the 1960s with the release of Typeleaf sheets containing Lorem Ipsum passages, and more recently with desktop publishing software like Pagecraft Studio including versions of Lorem Ipsum.</p>
    <p class="gap">is simply dummy text of the printing and typesetting industry. Lorem Ipsum has been the industry's standard dummy text ever since the 1500s, when an unknown printer took a galley of type and scrambled it to make</p>
    <p>is simply dummy text of the printing and typesetting industry. Lorem Ipsum has been the industry's standard dummy text ever since the 1500s, when an unknown printer took a galley of type and scrambled it to make a type specimen book. It has survived not only five centuries, but also the leap into electronic typesetting, remaining essentially unchanged. It was popularised in the 1960s with the release of Typeleaf sheets containing Lorem Ipsum passages, and more recently with desktop publishing software like Pagecraft Studio including versions of Lorem Ipsum.</p>
    <p>Best Regards,</p>
    <div class="signature" role="img" aria-label="Handwritten signature"></div>
    <p><strong>Darren Vale</strong><br>Director<br><br>ABC Building, def St., Country Name</p>
  </div>
  <div class="footer-band"></div>
</section>

<section class="sheet cover">
  <div class="brand"><span class="brand-name">Corvane Diamonds</span><span class="brand-mark"></span></div>
  <div class="footer-band"></div>
</section>

<section class="sheet card card-front">
  <div class="brand"><span class="brand-name">Corvane Diamonds</span><span class="brand-mark"></span></div>
  <div class="holder">
    <p class="name">ALDEN MARSH</p>
    <p class="role">Director - C.E.O</p>
    <p class="addr">Suite 8, 204 Rue Neuve<br>BE 2000</p>
  </div>
  <ul class="card-contacts">
    <li>+32 555 0147</li>
    <li>+32 555 0148</li>
    <li>+32 555 0149</li>
    <li>mail@corvane.com</li>
    <li>www.corvane.com</li>
  </ul>
  <div class="footer-band"></div>
</section>

<section class="sheet card card-back">
  <div class="brand"><span class="brand-name">Corvane Diamonds</span><span class="brand-mark"></span></div>
</section>

<section class="sheet envelope-front">
  <div class="brand"><span class="brand-name">Corvane Diamonds</span><span class="brand-mark"></span></div>
  <div class="footer-band"></div>
</section>

<section class="sheet envelope-back">
  <div class="flap"><span class="web">www.corvanediamonds.com</span></div>
</section>

</body>
</html>
```